Bright Path Mortgage team needs a booth

we are a mortgage company called WE FIND HOMES and our staff has caricatures designed in SUPER HERO style
we help people that have been turned down at other lenders get a second chance of buying a home
we want to be welcoming yet professional so that they know we take their needs seriously
our slogan is
We Find Homes
It's What We Do!

Industry/Entity Type

It Company

Font styles to use
Sans Serif

Colors
ec1f27
0355a3
fbed22

Requirements
Must have
• 1- 10 ft wide x 8ft high backdrop
• 2- 3ft wide x 8ft wide vertical banners
• 1 table cover 8 ft wide x 2.5 ft high
Nice to have
• i like modern and clean designs

```html
<!DOCTYPE html>
<html lang="en">
<head>
<meta charset="utf-8">
<title>We Find Homes – Booth Set</title>
<link rel="stylesheet" href="https://fonts.googleapis.com/css2?family=Roboto+Condensed:wght@400;700&display=swap">
<style>
  :root{
    --red:#ec1f27;
    --red-deep:#d8151d;
    --blue:#0355a3;
    --navy:#0b2f7a;
    --yellow:#fbed22;
    --yellow-soft:#eef15a;
    --gray:#c4c5c8;
    --strip:#e4e5e7;
    --white:#ffffff;
    --font:"Roboto Condensed", Arial, sans-serif;
  }
  *{box-sizing:border-box;margin:0;padding:0}
  html,body{width:1200px;height:796px;overflow:hidden;background:var(--white)}
  body{position:relative;font-family:var(--font)}
  .piece{position:absolute;overflow:hidden}
  .piece svg.bg{position:absolute;left:0;top:0;display:block}
  .abs{position:absolute}

  .side-banner{top:0;width:222px;height:590px}
  .side-banner.left{left:0}
  .side-banner.right{left:978px}
  .side-banner .hero-art{left:36px;top:12px;width:150px;height:236px;border-radius:40px 40px 20px 20px;
    background:linear-gradient(180deg,#3a3a3a 0%,#6d8fc4 55%,#c8393f 100%);opacity:.55}
  .side-banner.right .hero-art{left:38px}
  .side-banner .pitch{left:0;width:222px;text-align:center;color:var(--yellow);font-weight:700;
    font-size:22px;line-height:36px}
  .side-banner.left .pitch{top:268px}
  .side-banner.right .pitch{top:254px;line-height:33.5px}
  .side-banner .name-strip{left:0;top:391px;width:222px;height:55px;background:var(--strip);
    display:flex;align-items:center;justify-content:center}
  .name-strip .brand-name{color:var(--navy);font-weight:700;font-size:27px;line-height:27px;letter-spacing:-.3px}
  .side-banner .slogan{left:0;top:452px;width:222px;text-align:center;color:var(--yellow);
    font-weight:700;font-size:25px}

  .backdrop{left:230px;top:0;width:738px;height:590px}
  .backdrop .brand-name{left:0;top:40px;width:738px;text-align:center;color:var(--navy);
    font-weight:700;font-size:64px;line-height:64px;letter-spacing:-.5px}
  .backdrop .mission{left:0;top:436px;width:738px;text-align:center;color:var(--yellow);
    font-weight:700;font-size:25px;line-height:40px}

  .table-cover{left:304px;top:610px;width:590px;height:184px;
    background:radial-gradient(circle at 55% 40%,var(--red) 0%,var(--red-deep) 100%);border:1px solid #b9b9b9}
  .table-cover .hero-art{left:32px;top:6px;width:104px;height:174px;border-radius:36px 36px 16px 16px;
    background:linear-gradient(180deg,#3a3a3a 0%,#6d8fc4 55%,#b8353a 100%);opacity:.6}
  .table-cover .brand-name{left:200px;top:38px;width:330px;text-align:center;color:var(--navy);
    font-weight:700;font-size:44px;line-height:48px;letter-spacing:-.4px}
  .table-cover .slogan{left:200px;top:116px;width:330px;text-align:center;color:var(--white);
    font-weight:700;font-size:43px;line-height:52px}
</style>
</head>
<body>

<section class="piece side-banner left">
  <svg class="bg" width="222" height="590" viewBox="0 0 222 590">
    <rect width="222" height="590" fill="var(--gray)"/>
    <rect width="222" height="12" fill="var(--navy)"/>
    <path d="M0,172 Q110,232 222,246 L222,590 L0,590 Z" fill="var(--yellow-soft)"/>
    <path d="M0,182 Q110,242 222,256 L222,590 L0,590 Z" fill="var(--red)"/>
    <rect y="573" width="222" height="17" fill="var(--navy)"/>
  </svg>
  <div class="abs hero-art" role="img" aria-label="Cartoon caricature of a team member in a superhero costume holding a round shield"></div>
  <p class="abs pitch">Deal Falling Apart?<br>Don't Risk Losing<br>Your Commission!</p>
  <div class="abs name-strip"><span class="brand-name">WE FIND HOMES</span></div>
  <p class="abs slogan">IT'S WHAT WE DO!</p>
</section>

<section class="piece backdrop">
  <svg class="bg" width="738" height="590" viewBox="0 0 738 590">
    <defs>
      <linearGradient id="teamTone" x1="0" y1="0" x2="0" y2="1">
        <stop offset="0" stop-color="#3b3b3b" stop-opacity=".55"/>
        <stop offset=".5" stop-color="#f1c8b8" stop-opacity=".6"/>
        <stop offset="1" stop-color="#3f78b8" stop-opacity=".6"/>
      </linearGradient>
    </defs>
    <rect width="738" height="590" fill="var(--white)"/>
    <rect width="738" height="12" fill="#c4121a"/>
    <rect x="138" y="116" width="424" height="280" rx="30" fill="url(#teamTone)" role="img"
      aria-label="Cartoon caricatures of four team members in matching superhero costumes"/>
    <path d="M0,412 C120,330 250,300 370,335 S560,420 738,330 L738,590 L0,590 Z" fill="var(--yellow-soft)"/>
    <path d="M0,424 C120,342 250,312 370,347 S560,432 738,342 L738,590 L0,590 Z" fill="var(--red)"/>
    <rect y="573" width="738" height="17" fill="var(--navy)"/>
  </svg>
  <div class="abs brand-name">WE FIND HOMES</div>
  <p class="abs mission">We believe every family deserves the opportunity to own a home!<br>It is our mission to make that happen!</p>
</section>

<section class="piece side-banner right">
  <svg class="bg" width="222" height="590" viewBox="0 0 222 590">
    <rect width="222" height="590" fill="var(--gray)"/>
    <rect width="222" height="12" fill="var(--navy)"/>
    <path d="M0,240 Q110,232 222,172 L222,590 L0,590 Z" fill="var(--yellow-soft)"/>
    <path d="M0,250 Q110,242 222,182 L222,590 L0,590 Z" fill="var(--red)"/>
    <rect y="573" width="222" height="17" fill="var(--navy)"/>
  </svg>
  <div class="abs hero-art" role="img" aria-label="Cartoon caricature of a team member in a superhero costume with a round shield"></div>
  <p class="abs pitch">Want to buy a home?<br>Been turned down?<br>We can help you get<br>APPROVED!</p>
  <div class="abs name-strip"><span class="brand-name">WE FIND HOMES</span></div>
  <p class="abs slogan">IT'S WHAT WE DO!</p>
</section>

<section class="piece table-cover">
  <div class="abs hero-art" role="img" aria-label="Cartoon caricature of a team member flying in a superhero costume with a shield"></div>
  <div class="abs brand-name">WE FIND HOMES</div>
  <p class="abs slogan">IT'S WHAT WE DO!</p>
</section>

</body>
</html>
```